BRW Trifold Brochure

Would like a Trifold Brochure to use for marketing purposes. The company, Bright Ridge Works is a Handyman Service that offers Residential Home Repairs, Commercial Repairs, Drain Cleaning, Carpet Cleaning and Water Extraction.

I am attaching some pdf files to use as potential verbage and a copy of our business card and logo image file.

Would like to portray a professional image that sets us apart from a "mom and pops" type handyman service.

Industry/Entity Type

Marketing

```html
<!DOCTYPE html>
<html lang="en">
<head>
<meta charset="utf-8">
<title>Bright Ridge Works Trifold Brochure</title>
<link href="https://fonts.googleapis.com/css2?family=Open+Sans:ital,wght@0,400;0,600;0,700;1,400;1,600&display=swap" rel="stylesheet">
<style>
  :root {
    --navy: #0e1b3a;
    --navy-deep: #08122a;
    --blue: #1d4f9c;
    --sky: #7fb3e6;
    --ink: #1f1f1f;
    --silver: #c9ccd2;
    --white: #ffffff;
  }
  * { box-sizing: border-box; margin: 0; padding: 0; }
  html, body { width: 773px; height: 1200px; overflow: hidden; background: var(--white); }
  body { font-family: "Open Sans", Arial, sans-serif; color: var(--ink); }
  .brochure { position: relative; width: 773px; height: 1200px; overflow: hidden; }
  .backdrop { position: absolute; inset: 0; width: 773px; height: 1200px; }
  .block { position: absolute; }

  .brand-name { font-family: "Open Sans", Arial, sans-serif; font-weight: 700; color: var(--navy); letter-spacing: 0.5px; line-height: 1.05; text-align: center; }
  .brand-name.small { font-size: 22px; }

  .heading-blue { color: var(--blue); font-weight: 700; font-size: 14px; }
  .plain-list { list-style: none; font-size: 13px; line-height: 21px; margin-top: 6px; }

  .why-us { left: 17px; top: 145px; width: 240px; }
  .offers { left: 17px; top: 306px; width: 260px; }

  .contact { left: 256px; top: 236px; width: 260px; text-align: center; font-size: 11px; line-height: 15.5px; }
  .contact .heading-blue { font-size: 14px; margin-bottom: 6px; }
  .contact .office { font-weight: 700; }
  .contact .gap { margin-top: 18px; }
  .contact .hours { margin-top: 44px; font-size: 11.5px; }

  .logo-middle { left: 290px; top: 160px; width: 200px; }
  .house-art { left: 556px; top: 156px; width: 164px; height: 152px; background: linear-gradient(160deg, #3a3a3a, #0d0d0d); border-radius: 2px; }
  .logo-right { left: 540px; top: 362px; width: 200px; }
  .tagline { left: 530px; top: 430px; width: 220px; text-align: center; color: var(--blue); font-size: 12px; line-height: 15.5px; }

  .promo { left: 17px; top: 489px; width: 240px; color: var(--white); font-size: 11px; line-height: 14px; }
  .phone-big { left: 580px; top: 556px; font-size: 19px; font-weight: 700; color: var(--ink); }

  .logo-inside { left: 30px; top: 640px; width: 180px; }
  .handyman { left: 17px; top: 764px; width: 240px; color: var(--white); }
  .handyman h2 { font-size: 15px; font-weight: 700; margin-bottom: 7px; }
  .service-cols { display: grid; grid-template-columns: 137px 110px; row-gap: 10px; }
  .service-group h3 { color: var(--sky); font-style: italic; font-weight: 400; font-size: 12px; line-height: 14px; }
  .service-group ul { list-style: none; font-size: 10.5px; line-height: 13.6px; font-weight: 600; }

  .drain { left: 268px; top: 720px; width: 244px; color: var(--white); font-size: 10.2px; line-height: 13.4px; }
  .drain h2 { font-size: 14.5px; font-weight: 700; margin-bottom: 8px; }
  .drain h3 { color: var(--sky); font-style: italic; font-weight: 400; font-size: 12px; margin: 10px 0 4px; }
  .drain h3:first-of-type { margin-top: 0; }
  .faucet-photo { left: 256px; top: 1034px; width: 260px; height: 166px; background: radial-gradient(ellipse at 50% 30%, #9ed0f5 0%, #3d83c9 45%, #0f3f7a 100%); }

  .right-inside { left: 524px; top: 622px; width: 238px; font-size: 10.2px; line-height: 13.4px; }
  .right-inside h2 { font-size: 14.5px; font-weight: 700; line-height: 18px; color: var(--ink); margin-bottom: 10px; }
  .right-inside h3 { color: var(--blue); font-style: italic; font-weight: 400; font-size: 12px; margin: 0 0 3px; }
  .right-inside p { margin-bottom: 16px; }
  .right-inside .tile { margin-top: 20px; }
  .call-today { text-align: center; font-size: 18px; font-weight: 700; line-height: 22px; margin-top: 20px; }
</style>
</head>
<body>
<main class="brochure">
  <svg class="backdrop" viewBox="0 0 644 1000" preserveAspectRatio="none" aria-hidden="true">
    <defs>
      <linearGradient id="silver" x1="0" x2="1" y1="0" y2="0">
        <stop offset="0" stop-color="#e9ebee"/>
        <stop offset="0.5" stop-color="#9da2aa"/>
        <stop offset="1" stop-color="#eceef1"/>
      </linearGradient>
      <linearGradient id="navyShade" x1="0" x2="1" y1="0" y2="1">
        <stop offset="0" stop-color="#142550"/>
        <stop offset="1" stop-color="#08122a"/>
      </linearGradient>
    </defs>
    <path d="M0 0 H644 V42 C460 50 220 70 0 96 Z" fill="url(#navyShade)"/>
    <path d="M0 104 C220 78 460 58 644 52" fill="none" stroke="url(#silver)" stroke-width="7"/>
    <path d="M0 366 C200 385 430 405 644 410 V500 H0 Z" fill="url(#navyShade)"/>
    <path d="M0 374 C200 393 430 413 644 418" fill="none" stroke="url(#silver)" stroke-width="6"/>
    <path d="M300 500 C400 460 520 435 644 425 V500 Z" fill="#eceef1"/>
    <path d="M300 500 C400 460 520 435 644 425" fill="none" stroke="url(#silver)" stroke-width="5"/>
    <path d="M0 640 C150 622 320 565 430 505 V1000 H0 Z" fill="url(#navyShade)"/>
    <path d="M0 632 C150 614 320 558 430 498" fill="none" stroke="url(#silver)" stroke-width="7"/>
  </svg>

  <section class="block why-us">
    <h2 class="heading-blue">Why Choose Us?</h2>
    <ul class="plain-list">
      <li>Locally Owned and Operated</li>
      <li>Quality Drain Cleaning Services</li>
      <li>24 Hour Emergency Drain Service</li>
      <li>Affordable Pricing</li>
      <li>Warranty Provided</li>
    </ul>
  </section>

  <section class="block offers">
    <h2 class="heading-blue">Bright Ridge Works offers:</h2>
    <ul class="plain-list">
      <li>Handyman Services</li>
      <li>Carpet Cleaning and Water Extraction</li>
      <li>Tile and Grout Cleaning Services</li>
      <li>Drain Cleaning Services</li>
    </ul>
  </section>

  <div class="block logo-middle brand-name small">Bright Ridge Works</div>

  <section class="block contact">
    <h2 class="heading-blue">Contact Us:</h2>
    <p class="office">Our Office</p>
    <p>Bright Ridge Works</p>
    <p>410 Ridgeline Rd</p>
    <p>Marlow, KS 66600</p>
    <p class="gap">Email: info@brightridgeworks.com</p>
    <p>Phone: (555) 014 - 2290</p>
    <p class="hours">Available 24 Hours a day, 7 Days a week.</p>
  </section>

  <div class="block house-art" role="img" aria-label="Silhouette illustration of workers repairing a house"></div>
  <div class="block logo-right brand-name small">Bright Ridge Works</div>
  <p class="block tagline">The Services You Need.<br>The Quality you Expect.<br>Prices you can Afford.</p>

  <p class="block promo">Bright Ridge Works is the professional answer to your all of your home maintenance needs. Our courteous and knowledgable staff have the skills necessary to resolve your issues at a price that you can afford.</p>
  <p class="block phone-big">555-014-2290</p>

  <div class="block logo-inside brand-name small">Bright Ridge Works</div>

  <section class="block handyman">
    <h2>Handyman Services</h2>
    <div class="service-cols">
      <div class="service-group">
        <h3>Plumbing</h3>
        <ul><li>Faucets</li><li>Sinks</li><li>Toilets</li><li>Garbage Disposals</li><li>Hot Water Tanks</li><li>Shut Off Valves</li><li>Leaks</li></ul>
      </div>
      <div class="service-group">
        <h3>Electical</h3>
        <ul><li>Lighting</li><li>Outlets</li><li>Switches</li><li>GFCI</li><li>Ceiling Fans</li></ul>
      </div>
      <div class="service-group">
        <h3>HVAC &amp; Appliances</h3>
        <ul><li>Air Conditioning</li><li>Furnaces</li><li>Hot Water Heaters</li><li>Fridges</li><li>Stoves</li><li>Dishwashers</li></ul>
      </div>
      <div class="service-group">
        <h3>Interior Services</h3>
        <ul><li>Painting</li><li>Drywall Repair</li><li>Screens/Windows</li><li>Locks</li><li>Tile Repair</li><li>Tile/Grout Cleaning</li><li>Caulking</li><li>Handrails</li></ul>
      </div>
      <div class="service-group">
        <h3>Exterior Services</h3>
        <ul><li>Gutter Cleaning</li><li>Power Washing</li><li>Deck Repairs</li><li>Staining/Sealing</li><li>Wood Rot Repairs</li><li>Minor Roof Repairs</li></ul>
      </div>
    </div>
  </section>

  <section class="block drain">
    <h2>Drain Cleaning Services</h2>
    <h3>Diagnostic Capabilities</h3>
    <p>Our expert technicians have the knowledge and resources necessary to ensure a proper diagnosis of your drain problem. Our technicians will be able to determine where the blockage is, how to clear the blockage and in some cases what is causing the blockage.</p>
    <h3>The Right Equipment</h3>
    <p>Our technicians are equipped with the machinery necessary to clear your blocked sewer line wheather it is a bathroom lavatory or the main sewer line.</p>
    <h3>Service Area</h3>
    <p>Bright Ridge Works services Alder County and surrounding area's (Additional charges apply outside Alder County). We service Residential Homes, Commercial Buildings, Apartment Complexes and Rental Properties of all types.</p>
  </section>

  <div class="block faucet-photo" role="img" aria-label="Photo of water running from a chrome faucet"></div>

  <section class="block right-inside">
    <h2>Carpet Cleaning and<br>Water Extraction</h2>
    <h3>How Clean is your Carpet?</h3>
    <p>Carpet is one of the most used items in our household and yet is often the most ignored. Dirt, Sand, Food, Dander, Dead Skin, Hair, Grease and oil all build up over time. Sure you vacuum but is it doing enough? The answer is no! Let us take care of your carpet cleaning needs with our experienced technicans and the right equipment for the job.</p>
    <h3>Emergency Water Extraction</h3>
    <p>Water does serious damage. When there is an emergency, timing is of the essence. When that pipe breaks or a back up occurs call us and we'll be there. Our knowledgable staff and is equipped with the resources to give you the best chance of salvaging your carpet after a major water issue. We are available 24/7 for emergency water extraction!</p>
    <h2 class="tile">Tile and Grout Cleaning Services</h2>
    <p>You mop and you scrub but is that enough? With our tile and grout cleaning equipment you will truly be amazed with the results. Kitchen and bathroom tile, floor or wall and don't forget the grout. Give us a try, you won't regret it.</p>
    <p class="call-today">Call Today!<br>555- 014 - 2290</p>
  </section>
</main>
</body>
</html>
```